App-Design für Vergleichsportal für Reparaturen
Zielgruppe
Flickwerkstatt ist das Vergleichsportal für Reparaturen in deiner Nähe. Egal ob du eine Werkstatt für dein Smartphone, Tablet, Laptop, Computer, Smartwatch oder Spielkonsole suchst. Mit uns findest du deine passende Reparaturwerkstat in deiner Nähe mit dem besten Preis für dich. Du kannst dich direkt über unser Portal deinen Reparaturauftrag erhalten und wirst durch unser Sicher Kaufen Käuferschutz und unser MONVIRA Treuhandschutz abgesichert.
Aufgabenstellung
Unter Flickwerkstatt.de kann das aktuelle Design angeschaut werden. Die Farbe sollten übernommen werden.
Über die Startseite kann der Kunde sein Gerät, Service sowie seine Adresse eingeben. Auf der Vergleichsseite bekommt der Kunde die Übersicht welche Reparaturwerkstätten es gibt, zu welche Preisen die ausgewählte Dienstleistung angeboten wird. Wenn der Kunde auf den Button 'Jetzt Online Bestpreis buchen' drückt, dann kommt der Kunde in den Warenkorb. Im Warenkorb können noch weitere Dienstleistungen und Produkte dazugebucht werden. Und anschließend kommt der Kunde in die Kasse und kann der Bestellvorgang beenden. Die Benutzerführung sollte einfach sein. Im Fokus steht die Vergleichsseite. Dort sollte der Kunde ca. 4 Werkstätten auf einen Blick sehen können. Könnte ausschauen wie bei Wahlblick9 in der Kategorie Mobilfunk.
Die Vergleichseite sollte auf jeden Fall folgende Elemente enthalten:
- Entfernung zur Werkstatt in Meter bzw. Kilometer
- Logo der Werkstatt
- Name der Werkstatt
- Bewertungssterne der Werkstatt
- Reparaturzeit und Ersatzeilverfügbarkeit
- Reparaturpreis (Platz sollte auch bei Auswahl von 2 Dienstleistungen vorhanden sein)
- Rabattanzeige
- Qualitätssiegel (noch nicht vorhanden)
- Anzeige von Verknappung (z. B. noch 3 Termin frei)
- Qualitätsmerkmale (z. B. 12 Monate Garantie)
Die Merkmale Öffnungszeiten, Adresse, Kostenpflichtige Zusatzleistungen können aus Platzgründen in den Warenkorbseite wandern außer es gibt eine schöne und einfache Lösung.
In der Warenkorbseite kann dazu auch die Wahlblick9 Seite dienen.
Bei allen sollte auf die Benutzerfreundlichkeit geachtet werden.
Bei offenen Frage stehe ich zur Verfügung und freue mich auf viele Designs.
Vielen DANK im Voraus!

```html
<!DOCTYPE html>
<html lang="de">
<head>
<meta charset="utf-8">
<title>Flickwerkstatt – Vergleichsseite</title>
<link rel="stylesheet" href="https://fonts.googleapis.com/css2?family=Source+Sans+3:wght@300;400;600&display=swap">
<style>
  :root{
    --stage:#2a2a2a;
    --teal:#264a5c;
    --teal-line:#8fb3c4;
    --green:#8ab83a;
    --green-dark:#6f9a25;
    --red:#c8102e;
    --ink:#2d2d2d;
    --muted:#6b6b6b;
    --list-bg:#eef0f2;
    --white:#ffffff;
    --star-off:#d9d9d9;
    --star-on:#e6b800;
  }
  *{box-sizing:border-box;margin:0;padding:0}
  html,body{width:1200px;height:728px;overflow:hidden;background:var(--stage);font-family:"Source Sans 3",sans-serif;color:var(--ink)}
  .screen{position:absolute;left:439px;top:16px;width:402px;height:870px;transform:scale(.8);transform-origin:0 0;background:var(--white);overflow:hidden}
  .status-bar{height:30px;display:flex;justify-content:space-between;align-items:center;padding:0 14px 0 20px;font-weight:600;font-size:15px}
  .status-icons{display:flex;gap:5px;align-items:center}
  .app-header{height:57px;display:flex;justify-content:space-between;align-items:center;padding:0 14px 0 16px}
  .brand{display:flex;align-items:center;gap:6px;font-size:17px;font-weight:400;color:var(--teal)}
  .brand-dot{width:12px;height:12px;border-radius:50%;background:var(--green)}
  .menu-btn span{display:block;width:24px;height:2px;background:var(--teal);margin:6px 0}
  .hero-band{background:var(--teal);height:71px;text-align:center;padding-top:20px}
  .hero-title{color:var(--green);font-weight:600;font-size:13px}
  .hero-sub{color:var(--green);font-size:10.5px;margin-top:4px}
  .list{background:var(--list-bg);padding:12px 31px 0;height:712px}
  .crumbs{display:flex;justify-content:space-between;font-size:9.5px;margin:0 0 10px -1px;width:341px}
  .crumbs .edit{color:var(--green)}
  .card{background:var(--white);margin-bottom:18px}
  .dist-bar{background:var(--teal);height:31px;display:flex;align-items:center;justify-content:space-between;padding:0 10px;color:var(--white);font-size:12.5px;font-weight:300;border-bottom:2px solid var(--teal-line)}
  .card-body{padding:8px 12px 10px}
  .top-row{display:flex;justify-content:space-between}
  .shop-name{font-size:13.5px}
  .shop-logo{display:flex;align-items:center;gap:5px;font-size:15px;color:var(--teal);margin-top:6px}
  .shop-logo i{width:10px;height:10px;background:var(--teal)}
  .shop-logo.alt{color:#e36b1d}
  .shop-logo.alt i{background:#e36b1d;border-radius:50%}
  .rating{display:flex;align-items:center;gap:4px;margin-top:10px;color:var(--green);font-size:13px}
  .prices{text-align:right}
  .old-price{font-size:18px;text-decoration:line-through;color:var(--ink);margin-top:4px}
  .price{font-size:22px;color:var(--green);font-weight:400;line-height:1.1}
  .discount{display:inline-flex;align-items:center;gap:6px;background:var(--green);color:var(--white);font-size:8px;line-height:1.15;padding:4px 8px 4px 5px;margin-top:4px;text-align:left}
  .scarcity{display:flex;justify-content:space-between;align-items:center;background:var(--red);color:var(--white);font-size:11.5px;height:30px;padding:0 9px;margin:10px -4px 0}
  .scarcity span{display:flex;align-items:center;gap:7px}
  .facts{display:flex;align-items:flex-start;margin-top:10px;font-size:9.5px;line-height:1.3}
  .addr{display:flex;gap:4px;width:138px;border-right:1px solid #bdbdbd;margin-right:12px}
  .times{flex:1;display:grid;grid-template-columns:1fr auto}
  .times .val{color:var(--green);text-align:right}
  .times .val.no{color:var(--red)}
  .features{display:flex;justify-content:space-between;margin-top:9px}
  .feature{width:98px;height:30px;border:2px solid var(--teal);display:flex;align-items:center;font-size:7.5px;color:var(--green)}
  .feature svg{margin:0 6px 0 4px;flex:none}
  .feature.no{color:var(--red)}
  .feature .txt{flex:1;text-align:center;line-height:1.1;padding-right:3px}
  .book-btn{display:flex;align-items:center;justify-content:center;gap:8px;background:var(--green);color:var(--white);font-size:12.5px;height:35px;margin-top:12px;border-bottom:2px solid var(--green-dark)}
</style>
</head>
<body>
<svg width="0" height="0" style="position:absolute">
  <defs>
    <symbol id="star" viewBox="0 0 20 20"><polygon points="10,1 12.6,7 19,7.5 14,11.7 15.6,18.3 10,14.8 4.4,18.3 6,11.7 1,7.5 7.4,7"/></symbol>
    <symbol id="pin" viewBox="0 0 12 16"><path d="M6 0a6 6 0 0 0-6 6c0 4.5 6 10 6 10s6-5.5 6-10a6 6 0 0 0-6-6zm0 8.5A2.5 2.5 0 1 1 6 3.5a2.5 2.5 0 0 1 0 5z"/></symbol>
    <symbol id="flag" viewBox="0 0 14 14"><path d="M1 1h12l-3 4 3 4H3v5H1z"/></symbol>
    <symbol id="cart" viewBox="0 0 18 16"><path d="M0 1h3l2.5 9h9l2-6.5H5" fill="none" stroke="currentColor" stroke-width="1.5"/><circle cx="7" cy="13.5" r="1.5"/><circle cx="13" cy="13.5" r="1.5"/></symbol>
    <symbol id="truck" viewBox="0 0 22 14"><path d="M1 2h12v8H1zM13 5h4l3 3v2h-7z" fill="none" stroke="currentColor" stroke-width="1.4"/><circle cx="5" cy="11.5" r="1.8"/><circle cx="16" cy="11.5" r="1.8"/></symbol>
    <symbol id="gift" viewBox="0 0 18 18"><path d="M2 8h14v9H2zM1 5h16v3H1zM9 5v12M9 5C7 1 4 2 5 5M9 5c2-4 5-3 4 0" fill="none" stroke="currentColor" stroke-width="1.3"/></symbol>
    <symbol id="medal" viewBox="0 0 16 18"><circle cx="8" cy="7" r="6" fill="none" stroke="currentColor" stroke-width="1.4"/><circle cx="8" cy="7" r="3" fill="none" stroke="currentColor" stroke-width="1.2"/><path d="M4 12l-1 6 5-2 5 2-1-6" fill="none" stroke="currentColor" stroke-width="1.3"/></symbol>
  </defs>
</svg>

<main class="screen">
  <div class="status-bar">
    <span>9:41</span>
    <span class="status-icons">
      <svg width="16" height="10" viewBox="0 0 16 10"><rect x="0" y="7" width="3" height="3" fill="#222"/><rect x="4.5" y="5" width="3" height="5" fill="#222"/><rect x="9" y="2.5" width="3" height="7.5" fill="#222"/><rect x="13" y="0" width="3" height="10" fill="#222"/></svg>
      <svg width="15" height="11" viewBox="0 0 15 11"><path d="M7.5 10.5L5.5 8a3 3 0 0 1 4 0z M2.8 5.5a6.6 6.6 0 0 1 9.4 0l-1.3 1.4a4.7 4.7 0 0 0-6.8 0z M0 2.8a10.6 10.6 0 0 1 15 0l-1.3 1.3a8.7 8.7 0 0 0-12.4 0z" fill="#222"/></svg>
      <svg width="24" height="11" viewBox="0 0 24 11"><rect x=".5" y=".5" width="21" height="10" rx="2.5" fill="none" stroke="#222"/><rect x="2" y="2" width="18" height="7" rx="1.3" fill="#222"/><rect x="22.5" y="3.5" width="1.5" height="4" fill="#222"/></svg>
    </span>
  </div>

  <header class="app-header">
    <div class="brand"><span class="brand-dot"></span>Flickwerkstatt</div>
    <div class="menu-btn" aria-label="Menü"><span></span><span></span><span></span></div>
  </header>

  <section class="hero-band">
    <h1 class="hero-title">Reparaturen Im Vergleich, in deiner Nähe!</h1>
    <p class="hero-sub">Garantiert die besten Tarife</p>
  </section>

  <section class="list">
    <div class="crumbs">
      <span>Nexa 6s / Akku / Lindenplatz 4, München</span>
      <span class="edit">✎ Adresse ändern</span>
    </div>

    <article class="card">
      <div class="dist-bar">
        <svg width="11" height="15" fill="var(--green)"><use href="#pin"/></svg>
        <span>246 m von Dir entfernt</span>
        <svg width="13" height="13" fill="var(--green)"><use href="#flag"/></svg>
      </div>
      <div class="card-body">
        <div class="top-row">
          <div>
            <div class="shop-name">Kernfix München</div>
            <div class="shop-logo"><i></i>KERNFIX</div>
            <div class="rating">
              <svg width="16" height="16" fill="var(--star-on)"><use href="#star"/></svg>
              <svg width="16" height="16" fill="var(--star-on)"><use href="#star"/></svg>
              <svg width="16" height="16" fill="var(--star-on)"><use href="#star"/></svg>
              <svg width="16" height="16" fill="var(--star-on)"><use href="#star"/></svg>
              <svg width="16" height="16" fill="var(--star-on)"><use href="#star"/></svg>
              <span>(5/5)</span>
            </div>
          </div>
          <div class="prices">
            <div class="old-price">87,00€</div>
            <div class="price">79,00€</div>
            <div class="discount">
              <svg width="18" height="18" viewBox="0 0 18 18"><circle cx="9" cy="9" r="7.5" fill="none" stroke="#fff" stroke-width="1.3"/><text x="9" y="12" font-size="8" text-anchor="middle" fill="#fff" font-family="Source Sans 3, sans-serif">%</text></svg>
              <span>-8,00€ Rabatt<br>endet in 13h</span>
            </div>
          </div>
        </div>
        <div class="scarcity">
          <span>
            <svg width="10" height="14" viewBox="0 0 10 14"><path d="M1 1h8M1 13h8M2 1c0 4 6 4 6 6s-6 2-6 6M8 1c0 4-6 4-6 6s6 2 6 6" fill="none" stroke="#fff" stroke-width="1.3"/></svg>
            nur noch 3 Termine frei !
          </span>
          <svg width="13" height="12" viewBox="0 0 13 12"><path d="M6.5 0L13 12H0z" fill="#fff"/><rect x="5.8" y="4" width="1.4" height="4" fill="var(--red)"/><rect x="5.8" y="9" width="1.4" height="1.4" fill="var(--red)"/></svg>
        </div>
        <div class="facts">
          <div class="addr">
            <svg width="8" height="11" fill="var(--green)"><use href="#pin"/></svg>
            <span>Amselweg 12<br>80339 München</span>
          </div>
          <div class="times">
            <span>Reparaturzeit:</span><span class="val">2 Tage</span>
            <span>Ersatzteilverfügbarkeit:</span><span class="val">Verfügbar</span>
          </div>
        </div>
        <div class="features">
          <div class="feature"><svg width="20" height="13" fill="var(--teal)" color="var(--teal)"><use href="#truck"/></svg><span class="txt">Versand möglich</span></div>
          <div class="feature"><svg width="16" height="16" fill="var(--teal)" color="var(--teal)"><use href="#gift"/></svg><span class="txt">12 Monate Garantie</span></div>
          <div class="feature"><svg width="15" height="17" color="var(--teal)"><use href="#medal"/></svg><span class="txt">Muster Siegel</span></div>
        </div>
        <div class="book-btn"><svg width="17" height="15" fill="#fff" color="#fff"><use href="#cart"/></svg>Jetzt Online Bestpreis buchen</div>
      </div>
    </article>

    <article class="card">
      <div class="dist-bar">
        <svg width="11" height="15" fill="var(--green)"><use href="#pin"/></svg>
        <span>762 m von Dir entfernt</span>
        <svg width="13" height="13" fill="var(--green)"><use href="#flag"/></svg>
      </div>
      <div class="card-body">
        <div class="top-row">
          <div>
            <div class="shop-name">Handypraxis München Giesing</div>
            <div class="shop-logo alt"><i></i>Handypraxis</div>
            <div class="rating">
              <svg width="16" height="16" fill="var(--star-on)"><use href="#star"/></svg>
              <svg width="16" height="16" fill="var(--star-on)"><use href="#star"/></svg>
              <svg width="16" height="16" fill="var(--star-on)"><use href="#star"/></svg>
              <svg width="16" height="16" viewBox="0 0 20 20"><defs><linearGradient id="half"><stop offset=".55" stop-color="#e6b800"/><stop offset=".55" stop-color="#d9d9d9"/></linearGradient></defs><polygon points="10,1 12.6,7 19,7.5 14,11.7 15.6,18.3 10,14.8 4.4,18.3 6,11.7 1,7.5 7.4,7" fill="url(#half)"/></svg>
              <svg width="16" height="16" fill="var(--star-off)"><use href="#star"/></svg>
              <span>(3,7/5)</span>
            </div>
          </div>
          <div class="prices">
            <div class="price" style="margin-top:16px">82,00€</div>
          </div>
        </div>
        <div class="facts" style="margin-top:14px">
          <div class="addr">
            <svg width="8" height="11" fill="var(--green)"><use href="#pin"/></svg>
            <span>Amselweg 12<br>80339 München</span>
          </div>
          <div class="times">
            <span>Reparaturzeit:</span><span class="val">2 Tage</span>
            <span>Ersatzteilverfügbarkeit:</span><span class="val no">nicht verfügbar</span>
          </div>
        </div>
        <div class="features">
          <div class="feature no"><svg width="20" height="13" fill="var(--teal)" color="var(--teal)"><use href="#truck"/></svg><span class="txt">Versand nicht möglich</span></div>
          <div class="feature"><svg width="16" height="16" fill="var(--teal)" color="var(--teal)"><use href="#gift"/></svg><span class="txt">12 Monate Garantie</span></div>
          <div class="feature"><svg width="15" height="17" color="var(--teal)"><use href="#medal"/></svg><span class="txt">Muster Siegel</span></div>
        </div>
        <div class="book-btn"><svg width="17" height="15" fill="#fff" color="#fff"><use href="#cart"/></svg>Jetzt Online Bestpreis buchen</div>
      </div>
    </article>

    <article class="card">
      <div class="dist-bar">
        <svg width="11" height="15" fill="var(--green)"><use href="#pin"/></svg>
        <span>1.2 km von Dir entfernt</span>
        <svg width="13" height="13" fill="var(--green)"><use href="#flag"/></svg>
      </div>
      <div class="card-body">
        <div class="top-row">
          <div class="shop-name" style="margin-top:4px">Zellwerk am Harras</div>
          <div class="old-price">100,00€</div>
        </div>
      </div>
    </article>
  </section>
</main>
</body>
</html>
```